Business cards and stationary for zombie fantasy camp
The Bramble Lodge
Business cards and stationary for zombie fantasy camp - Outdoors
Creative Brief
Simple
Dwight Palmer
2648 Wendel Rd Copley Oh 44329
Dwight@thebramblelodge.example
www.thebramblelodge.example
Please refer to the website to get ideas as to what to add to this business card. I would like a design that speaks to the nature of the business. I have also uploaded 4 different logo's that I use, please feel free to experiment with each one. I'm in need of business cards, stationary, presentation folders, etc...
Please refer to the website to get ideas as to what to add to this business card. I would like a design that speaks to the nature of the business.
Tovick88 Tovick88
Attention please all designers: I've extended this contest for 3 days, not so much to find new designs but many of you have submitted designs that are nearing what I'm looking for. And the three days will enable us all time to communicate and work through those changes. I don't want any of you missing out because I didn't get online until only the final hours risking being able to give you all a chance to make those modifications I'm looking for. Sorry for the delay, But, thank you for your patience and all of your work.
All designers please note, you each that have submitted ideas have some excellent business card ideas, There is only 1 day left, please stop concentrating on business cards, and start focusing on stationary, letterheads, envelopes, and email signatures, I'm looking for the whole package here.
Just a quick message to thank everyone for the work that they have put into my project, I've got some excellent designs. With that being said, I still would like to see more designs for items specifically with Presentation Folders, Stationary, envelopes, and email signatures
Feel free to use any logo that I have uploaded here. I like all of them, so I look forward to seeing what you can do with any one of them or all of them.
My project had started once before, quillhaven had noticed that I had a logo project running at the same time, so they made the recommendation to put this on hold until that project finished. To the designers that submitted already, I apologize to you all. The logo project is now finished, I had multiple logo's I likes so I've posted them here for you to use as your inspiration. Good luck to you all and with all projects, I look forward to seeing your work.
I will be looking to use these designs when ordering business cards through prenta nook.example, I'm also looking for designs for stationary, envelopes and presentation folders all ordered through prentanook.example

```html
<!DOCTYPE html>
<html lang="en">
<head>
<meta charset="utf-8">
<title>The Bramble Lodge – Business Card</title>
<link href="https://fonts.googleapis.com/css2?family=Arimo:wght@400;700&display=swap" rel="stylesheet">
<style>
  :root {
    --backdrop: #e9e6e1;
    --card: #ffffff;
    --ink: #1e1e1e;
    --ink-soft: #6b6b6b;
    --gold-light: #f6c21a;
    --gold: #e3a500;
    --gold-deep: #9a7a10;
    --swoosh: #151515;
    --swoosh-edge: #bdbdbd;
  }
  * { margin: 0; padding: 0; box-sizing: border-box; }
  html, body {
    width: 1200px; height: 468px; overflow: hidden;
    background: var(--backdrop);
    font-family: "Arimo", Arial, sans-serif;
  }
  .stage { position: relative; width: 1200px; height: 468px; }
  .card {
    position: absolute; top: 30px; width: 564px; height: 408px;
    background: var(--card); overflow: hidden;
    box-shadow: 0 2px 8px rgba(0,0,0,.18);
  }
  .card--front { left: 24px; }
  .card--back { left: 612px; }

  .ghost-figure {
    position: absolute; left: 150px; top: 10px; width: 110px; height: 230px;
    background: linear-gradient(180deg, rgba(217,217,217,.55), rgba(217,217,217,.15));
    border-radius: 40px 40px 10px 10px;
  }
  .brand-mark {
    position: absolute; display: flex; align-items: center; gap: 10px;
    color: var(--ink); font-weight: 700; line-height: 1.05;
  }
  .brand-mark__square { width: 18px; height: 18px; background: var(--gold); flex: none; }
  .card--front .brand-mark { left: 36px; top: 60px; font-size: 26px; width: 200px; }
  .card--back .brand-mark {
    left: 50%; top: 50%; transform: translate(-50%, -50%);
    font-size: 36px; white-space: nowrap;
  }
  .card--back .brand-mark__square { width: 24px; height: 24px; }

  .holder-name {
    position: absolute; right: 30px; top: 26px;
    font-size: 21px; color: var(--ink-soft); font-weight: 400;
  }
  .waves { position: absolute; left: 0; top: 0; }
  .contact {
    position: absolute; right: 22px; text-align: right; color: var(--ink);
    font-size: 12.5px; line-height: 1.45;
  }
  .contact--address { top: 250px; }
  .contact--lines { top: 318px; }
</style>
</head>
<body>
<main class="stage">
  <section class="card card--front" aria-label="Business card front">
    <div class="ghost-figure" role="img" aria-label="Faint background silhouette of a camp figure"></div>
    <div class="brand-mark"><span class="brand-mark__square"></span><span>The Bramble Lodge</span></div>
    <p class="holder-name">Dwight Palmer</p>
    <svg class="waves" width="564" height="408" viewBox="0 0 564 408" aria-hidden="true">
      <defs>
        <linearGradient id="goldBand" x1="0" y1="0" x2="1" y2="0">
          <stop offset="0" stop-color="#9a7a10"/>
          <stop offset=".45" stop-color="#e3a500"/>
          <stop offset="1" stop-color="#f6c21a"/>
        </linearGradient>
      </defs>
      <path d="M0 248 C200 318 380 228 564 125 L564 131 C380 238 200 328 0 256 Z" fill="var(--swoosh-edge)"/>
      <path d="M0 260 C200 325 380 235 564 135 L564 165 C380 260 200 355 0 290 Z" fill="var(--swoosh)"/>
      <path d="M0 335 C180 390 380 290 564 190 L564 408 L0 408 Z" fill="url(#goldBand)"/>
    </svg>
    <p class="contact contact--address">2648 Wendel Rd<br>Copley Oh 44329</p>
    <p class="contact contact--lines">Phone:330-555-0142<br>Email: Dwight@thebramblelodge.example<br>Web: www.thebramblelodge.example</p>
  </section>

  <section class="card card--back" aria-label="Business card back">
    <div class="brand-mark"><span class="brand-mark__square"></span><span>The Bramble Lodge</span></div>
  </section>
</main>
</body>
</html>
```